#LUMA

#Luma is the business name. I need a marketing brochure to show potential clients. The concept is providing the restaurant trade and function centres with volume wine in large wine casks and then on-sell by the glass or in varying carafe sizes. The advantages will be outlined in the file provided I want to introduce the concept and demonstrate the advantages visusally

Restaurant

```html
<!DOCTYPE html>
<html lang="en">
<head>
<meta charset="utf-8">
<title>#Luma – Brochure Front</title>
<link rel="stylesheet" href="https://fonts.googleapis.com/css2?family=Crimson+Pro:ital,wght@0,400;0,700;1,700&family=Berkshire+Swash&display=swap">
<style>
  :root {
    --stage-light: #8c0054;
    --stage-dark: #3a0024;
    --band-top: #050003;
    --band-bottom: #5a0a3a;
    --wood-light: #5a3a22;
    --wood-dark: #3b2413;
    --cream-light: #f8eadc;
    --cream-dark: #ead3bc;
    --gold: #c99a2e;
    --gold-light: #ecc766;
    --peach: #f2c6a2;
    --maroon: #7a0f45;
    --ink: #2a1208;
    --white: #ffffff;
    --sketch: #c7ab93;
  }
  * { box-sizing: border-box; margin: 0; padding: 0; }
  html, body {
    width: 910px; height: 1200px; overflow: hidden;
  }
  body {
    position: relative;
    background: radial-gradient(ellipse at 75% 60%, var(--stage-light) 0%, #6a003f 45%, var(--stage-dark) 100%);
    font-family: "Crimson Pro", Georgia, serif;
  }
  .sheet-label {
    position: absolute; top: 38px; left: 0; width: 100%;
    text-align: center; color: var(--white);
    font: italic 700 14px "Crimson Pro", Georgia, serif;
    letter-spacing: 0.5px;
  }
  .brochure {
    position: absolute; left: 86px; top: 77px; width: 743px; height: 1043px;
    box-shadow: 0 28px 30px -14px rgba(0,0,0,0.7);
  }
  .brochure__band {
    position: absolute; left: 0; top: 0; width: 100%; height: 133px;
    background: linear-gradient(to bottom, var(--band-top), var(--band-bottom));
  }
  .brochure__wood {
    position: absolute; left: 0; top: 133px; width: 100%; height: 384px;
    background: linear-gradient(to bottom, var(--wood-light), var(--wood-dark));
  }
  .brochure__arc {
    position: absolute; left: 0; top: 0; width: 743px; height: 200px;
  }
  .brochure__arc text {
    font-family: "Berkshire Swash", cursive;
    font-size: 31px; fill: var(--peach);
  }
  .brand-name {
    position: absolute; left: 0; top: 160px; width: 100%;
    text-align: center; color: var(--gold-light);
    font: 700 96px/1 "Crimson Pro", Georgia, serif;
  }
  .tagline {
    position: absolute; left: 0; top: 412px; width: 100%;
    text-align: center; color: var(--white);
    font: 400 25px/32px "Crimson Pro", Georgia, serif;
  }
  .brochure__lower {
    position: absolute; left: 0; top: 517px; width: 100%; height: 526px;
    background: linear-gradient(to bottom, var(--cream-light), var(--cream-dark));
    overflow: hidden;
  }
  .vineyard-scene {
    position: absolute; left: 0; bottom: 0; width: 100%; height: 300px;
    background: linear-gradient(to bottom, rgba(199,171,147,0) 0%, rgba(199,171,147,0.35) 45%, rgba(199,171,147,0.5) 100%);
  }
  .gold-frame {
    position: absolute; left: 58px; top: 0; width: 636px; height: 482px;
    border: 7px solid var(--gold);
    border-top: none;
    box-shadow: inset 0 0 0 1px var(--gold-light);
  }
  .advantages {
    position: absolute; left: 0; top: 50px; width: 100%; text-align: center;
  }
  .advantages__title {
    color: var(--maroon);
    font: 700 25px/1 "Crimson Pro", Georgia, serif;
    margin-bottom: 28px;
  }
  .advantages__list { list-style: none; }
  .advantages__list li {
    color: var(--ink);
    font: italic 700 24px/45px "Crimson Pro", Georgia, serif;
  }
</style>
</head>
<body>
  <p class="sheet-label">BROCHURE FRONT</p>

  <article class="brochure">
    <div class="brochure__band"></div>
    <div class="brochure__wood" role="img" aria-label="Dark wooden plank background"></div>

    <svg class="brochure__arc" viewBox="0 0 743 200" aria-hidden="false">
      <path id="arc-path" d="M 195 125 Q 370 -5 545 125" fill="none"/>
      <text text-anchor="middle"><textPath href="#arc-path" startOffset="50%">Selected and imported by</textPath></text>
    </svg>

    <h1 class="brand-name">#Luma</h1>

    <p class="tagline">Providing the restaurant trade with a more effective,<br>economical and sustainable alternative to wine retail.</p>

    <section class="brochure__lower">
      <div class="vineyard-scene" role="img" aria-label="Faint sketch of a hillside vineyard with cypress trees and a farmhouse"></div>
      <div class="gold-frame"></div>
      <div class="advantages">
        <h2 class="advantages__title">The advantages of using #LUMA concept:</h2>
        <ul class="advantages__list">
          <li>*The cask wine uses less storage space</li>
          <li>*Eco friendly, no glass.</li>
          <li>*Larger quantity better margins</li>
          <li>*Longer shelf life</li>
          <li>*No wastage</li>
          <li>*More Hygienic</li>
        </ul>
      </div>
    </section>
  </article>
</body>
</html>
```